CREATE A BUSINESS CARD FOR A BOAT CLEANING SERVICE

WE ARE STARTING A NEW BOAT CLEANING BUSINESS. WE DIVE UNDERWATER TO CLEAN BOAT HULLS, JETTIES, UNDERWATER STRUCTURES ETC. WE ARE LOOKING FOR AN UPPERMARKET MODERN LOGO AND BUSINESS CARD AS ALOT OF OUR TARGET MARKET WILL BE HIGH END. YOU HAVE TO DESIGN A BUSINESS CARD AND LOGO SEPERATELY .
THE BUSINESS CARD DIMESNION MUST BE STANDARD SIZE.
The standard dimensions of a printed business card are 3.5 x 2 inches

Target Market(s)

UNDERWATER SERVICED

Industry/Entity Type

Business

Contact Information for Business Card

HALDANE SUBSEA SERVICES

Font styles to use
Serif

Colors

Designer to choose colors to be used in the design.

Requirements
Must have
• HALDANE
Nice to have
• dark
Should not have
• more than 3 colors

```html
<!DOCTYPE html>
<html lang="en">
<head>
<meta charset="utf-8">
<title>Haldane Subsea Services – Business Card</title>
<link href="https://fonts.googleapis.com/css2?family=Josefin+Sans:wght@300;400;600&family=Roboto:wght@300;400;500&display=swap" rel="stylesheet">
<style>
  :root {
    --navy: #0f5185;
    --grey: #8c8f93;
    --paper: #ffffff;
    --ink-soft: #9a9da1;
    --backdrop: #e9e8e6;
  }
  * { box-sizing: border-box; margin: 0; padding: 0; }
  html, body { width: 1200px; height: 930px; overflow: hidden; background: var(--backdrop); }
  .sheet { position: relative; width: 1200px; height: 930px; }

  .card {
    position: absolute; width: 560px; height: 320px; border-radius: 16px;
    overflow: hidden; box-shadow: 0 6px 18px rgba(0,0,0,.18);
  }
  .card--front { left: 70px; top: 110px; background: var(--navy); }
  .card--back { left: 570px; top: 500px; background: var(--paper); }

  .wordmark { position: absolute; font-family: "Josefin Sans", sans-serif; }
  .wordmark__name { font-weight: 400; letter-spacing: .42em; line-height: 1; }
  .wordmark__tag { font-weight: 300; letter-spacing: .26em; line-height: 1; margin-top: 10px; }

  .card--front .wordmark { left: 0; right: 0; top: 128px; text-align: center; color: var(--paper); }
  .card--front .wordmark__name { font-size: 40px; padding-left: .42em; }
  .card--front .wordmark__tag { font-size: 18px; padding-left: .26em; }

  .back-bands { position: absolute; inset: 0; }

  .holder { position: absolute; right: 28px; top: 22px; text-align: right; color: var(--paper); font-family: "Roboto", sans-serif; }
  .holder__name { font-size: 24px; font-weight: 500; letter-spacing: .01em; }
  .holder__role { font-size: 13px; font-weight: 300; margin-top: 2px; }

  .card--back .wordmark { left: 36px; top: 172px; color: var(--navy); }
  .card--back .wordmark__name { font-size: 30px; }
  .card--back .wordmark__tag { font-size: 14px; color: var(--ink-soft); margin-top: 8px; }

  .badges { position: absolute; right: 40px; top: 138px; display: flex; gap: 16px; align-items: center; }
  .badge { width: 38px; height: 38px; border-radius: 50%; background: var(--navy); }
  .badge--grey { background: var(--grey); }

  .rule { position: absolute; left: 36px; right: 28px; top: 238px; height: 1.5px; background: var(--navy); }

  .contacts { position: absolute; right: 28px; top: 186px; list-style: none; font-family: "Roboto", sans-serif; font-size: 13px; color: var(--ink-soft); text-align: right; line-height: 16px; }
  .contacts li { display: flex; justify-content: flex-end; align-items: center; gap: 8px; }
  .contacts svg { width: 10px; height: 10px; fill: none; stroke: var(--navy); stroke-width: 1.6; }

  .address { position: absolute; left: 36px; top: 256px; font-family: "Roboto", sans-serif; font-size: 14px; color: var(--ink-soft); line-height: 18px; }
</style>
</head>
<body>
<main class="sheet">

  <section class="card card--front" aria-label="Card front">
    <div class="wordmark">
      <p class="wordmark__name">HALDANE</p>
      <p class="wordmark__tag">SUBSEA SERVICES</p>
    </div>
  </section>

  <section class="card card--back" aria-label="Card back">
    <svg class="back-bands" viewBox="0 0 560 320" preserveAspectRatio="none" aria-hidden="true">
      <path d="M0,0 H560 V78 C500,150 380,138 260,112 C170,94 80,88 0,120 Z" fill="var(--navy)"/>
      <path d="M0,120 C80,88 170,94 260,112 C380,138 500,150 560,78 V96 C500,162 380,150 260,124 C170,106 80,104 0,140 Z" fill="var(--grey)"/>
      <path d="M0,146 C60,118 120,110 190,114 C120,116 60,130 20,168 L0,178 Z" fill="var(--navy)"/>
    </svg>

    <div class="holder">
      <p class="holder__name">MARCUS REID</p>
      <p class="holder__role">President</p>
    </div>

    <div class="wordmark">
      <p class="wordmark__name">HALDANE</p>
      <p class="wordmark__tag">SUBSEA SERVICES</p>
    </div>

    <div class="badges" aria-hidden="true">
      <span class="badge badge--grey"></span>
      <span class="badge"></span>
    </div>

    <ul class="contacts">
      <li>(555) 201-4380
        <svg viewBox="0 0 10 10"><path d="M2 1 L4 3 L3 4.5 Q4.5 6.5 5.5 7 L7 6 L9 8 L7.5 9.2 Q3 8 0.8 2.5 Z"/></svg></li>
      <li>info@haldanesubsea.com
        <svg viewBox="0 0 10 10"><rect x="1" y="2" width="8" height="6"/><path d="M1 2 L5 5.5 L9 2"/></svg></li>
      <li>www.haldanesubsea.com
        <svg viewBox="0 0 10 10"><circle cx="5" cy="5" r="4"/><path d="M1 5 H9 M5 1 Q2.5 5 5 9 Q7.5 5 5 1"/></svg></li>
    </ul>

    <div class="rule"></div>

    <address class="address" style="font-style:normal">
      310, 418- 9th Ave, SW<br>
      Kelmont, AB T4K 2M6
    </address>
  </section>

</main>
</body>
</html>
```